Re-design a website for a millionaire mentor

We need an expert website designer to re-design the website qBrightvoyage.com

The website would have 4 pages. A home page, Summit Circle page, Book RM page and an About page.

Here are some reference websites

https://www.kdmotivates.example
https://dorvalenm.example/

I will also attach a beginning of mockup of the home page I did myself to give an idea of the style we like, please use the quote "If you are not chasing your potential you are wasting your life" instead of the one in the current website...

You don't have the use the mockup (just the quote) and are free to use all your creativity.

Target Market(s)

Entrepreneurs

Number of Pages Required

4 page

Font styles to use
Other font styles liked:
• Franklin Gothic

Requirements
Must have
• -Call of action on the main page to download a free business plan
• -Book rm page check out reference: http://www.bookdorianvale.example
• -summit circle page with a button to sign in or join the summit circle. Check out reference for example: https://www.kdmotivates.example/pulse_academy

```html
<!DOCTYPE html>
<html lang="en">
<head>
<meta charset="utf-8">
<title>Bright Voyage</title>
<link rel="stylesheet" href="https://fonts.googleapis.com/css2?family=Poppins:wght@400;500;600;700&family=Permanent+Marker&display=swap">
<style>
  :root {
    --black: #000000;
    --white: #ffffff;
    --red: #ec3237;
    --red-bright: #f41518;
    --text-dark: #333333;
    --photo-dark: #1c1c1c;
    --photo-green: #3a5a3a;
  }
  * { margin: 0; padding: 0; box-sizing: border-box; }
  html, body { width: 1200px; height: 2192px; overflow: hidden; }
  body { position: relative; background: var(--white); font-family: 'Poppins', sans-serif; color: var(--white); }

  .hero { position: absolute; left: 0; top: 0; width: 1200px; height: 820px; }
  .hero-shape { position: absolute; left: 0; top: 0; }

  .brand { position: absolute; left: 88px; top: 26px; font-weight: 600; font-size: 38px; line-height: 46px; color: var(--white); letter-spacing: 1px; text-transform: uppercase; }

  .main-nav { position: absolute; top: 62px; left: 0; width: 1200px; height: 24px; }
  .main-nav a { position: absolute; font-size: 17px; font-weight: 500; color: var(--white); text-decoration: none; text-transform: uppercase; white-space: nowrap; }

  .hero-quote { position: absolute; left: 91px; top: 320px; font-size: 26px; line-height: 42px; text-transform: uppercase; font-weight: 400; }
  .hero-quote .accent { font-family: 'Permanent Marker', cursive; color: var(--red-bright); font-size: 24px; }

  .hero-cta { position: absolute; left: 91px; top: 452px; width: 282px; height: 81px; background: var(--red); display: flex; align-items: center; justify-content: space-between; padding: 0 22px; font-size: 26px; font-weight: 500; text-transform: uppercase; }

  .about-photo { position: absolute; left: 267px; top: 944px; width: 839px; height: 449px; background: linear-gradient(120deg, var(--photo-green) 0%, #2c4a30 45%, #1f3324 100%); }
  .about-card { position: absolute; left: 95px; top: 1008px; width: 411px; height: 331px; background: var(--white); border-left: 4px solid var(--red); padding: 26px 24px 0 24px; }
  .about-card h2 { font-size: 41px; font-weight: 600; color: var(--red); line-height: 48px; }
  .about-card p { margin-top: 8px; font-size: 15px; line-height: 34px; color: var(--text-dark); }
  .read-more { position: absolute; left: 24px; top: 255px; width: 163px; height: 47px; border-radius: 24px; background: var(--red); color: var(--white); font-size: 16px; font-weight: 600; display: flex; align-items: center; justify-content: center; }

  .footer-shape { position: absolute; left: 0; top: 1510px; }
  .footer { position: absolute; left: 0; top: 1656px; width: 1200px; height: 536px; background: var(--black); }
  .footer h3 { position: absolute; top: 68px; font-size: 23px; font-weight: 600; }
  .info-links { position: absolute; left: 100px; top: 120px; list-style: none; }
  .info-links li { font-size: 16px; font-weight: 500; line-height: 32px; }
  .social { position: absolute; top: 305px; width: 32px; height: 32px; border: 2px solid var(--white); border-radius: 50%; }
  .contact-item { position: absolute; left: 392px; display: flex; gap: 16px; font-size: 16px; line-height: 25px; font-weight: 500; }
  .contact-item svg { flex: none; margin-top: 2px; }
  .contact-item strong { font-weight: 600; }
  .field { position: absolute; left: 792px; width: 317px; height: 29px; border: 2px solid var(--white); font-size: 10px; padding: 6px 10px; line-height: 13px; }
  .submit { position: absolute; left: 792px; top: 333px; width: 184px; height: 35px; background: var(--red); font-size: 16px; font-weight: 600; display: flex; align-items: center; justify-content: center; }
  .copyright { position: absolute; left: 0; top: 462px; width: 1200px; text-align: center; font-size: 16px; font-weight: 500; }
</style>
</head>
<body>

<header class="hero">
  <svg class="hero-shape" width="1200" height="820" viewBox="0 0 1200 820">
    <defs>
      <linearGradient id="speakerTone" x1="0" y1="0" x2="1" y2="1">
        <stop offset="0" stop-color="#2a2a2a"/>
        <stop offset="1" stop-color="#0d0d0d"/>
      </linearGradient>
    </defs>
    <polygon points="0,0 1200,0 1200,684 842,812 0,678" fill="var(--black)"/>
    <polygon points="600,110 1200,110 1200,684 842,795 600,760" fill="url(#speakerTone)" role="img" aria-label="Photo of the mentor speaking on stage with a microphone"/>
    <polygon points="0,678 842,790 1200,684 1200,690 842,812 0,684" fill="var(--red-bright)"/>
  </svg>

  <div class="brand">Bright<br>Voyage</div>

  <nav class="main-nav">
    <a style="left:557px">Home</a>
    <a style="left:646px">Summit Circle</a>
    <a style="left:803px">Book RM</a>
    <a style="left:912px">About</a>
    <a style="left:1008px">Contact Us</a>
  </nav>

  <h1 class="hero-quote">If you are not chasing your <span class="accent">potential</span><br>You are <span class="accent">wasting</span> your life</h1>

  <div class="hero-cta">
    <svg width="18" height="30" viewBox="0 0 18 30"><polyline points="15,2 3,15 15,28" fill="none" stroke="var(--white)" stroke-width="3"/></svg>
    <span>Click Here</span>
    <svg width="18" height="30" viewBox="0 0 18 30"><polyline points="3,2 15,15 3,28" fill="none" stroke="var(--white)" stroke-width="3"/></svg>
  </div>
</header>

<section>
  <div class="about-photo" role="img" aria-label="Portrait of the mentor seated outdoors in front of green foliage"></div>
  <div class="about-card">
    <h2>About Us</h2>
    <p>Reid Marlow is CEO and Founder to one of the world's fastest growing IT Consulting companies in the world, according to Venture Weekly. Starting with only a few key employees,</p>
    <div class="read-more">Read More</div>
  </div>
</section>

<svg class="footer-shape" width="1200" height="150" viewBox="0 0 1200 150">
  <polygon points="0,142 358,13 1200,144 1200,150 0,150" fill="var(--red-bright)"/>
  <polygon points="0,150 358,30 1200,148 1200,150" fill="var(--black)"/>
</svg>

<footer class="footer">
  <h3 style="left:99px">Information</h3>
  <ul class="info-links">
    <li>Home</li>
    <li>About Us</li>
    <li>Summit Circle</li>
    <li>Book RM</li>
    <li>Contact Us</li>
  </ul>
  <span class="social" style="left:95px"></span>
  <span class="social" style="left:143px"></span>
  <span class="social" style="left:191px"></span>

  <h3 style="left:403px">Contact Us</h3>
  <div class="contact-item" style="top:128px">
    <svg width="32" height="32" viewBox="0 0 32 32"><circle cx="16" cy="16" r="14" fill="none" stroke="var(--white)" stroke-width="2"/><path d="M16 8a5 5 0 0 0-5 5c0 4 5 10 5 10s5-6 5-10a5 5 0 0 0-5-5z" fill="var(--white)"/><circle cx="16" cy="13" r="2" fill="var(--black)"/></svg>
    <span>780 Harbor Lane Suite<br>#214 Fairview, OR 97012</span>
  </div>
  <div class="contact-item" style="top:198px">
    <svg width="32" height="32" viewBox="0 0 32 32"><circle cx="16" cy="16" r="14" fill="none" stroke="var(--white)" stroke-width="2"/><path d="M11 9l3 0 1 4-2 1c1 2 3 4 5 5l1-2 4 1 0 3c-6 1-13-6-12-12z" fill="var(--white)"/></svg>
    <span>Call Us :<br><strong>+1 555 014 2290</strong></span>
  </div>
  <div class="contact-item" style="top:262px">
    <svg width="32" height="32" viewBox="0 0 32 32"><circle cx="16" cy="16" r="14" fill="none" stroke="var(--white)" stroke-width="2"/><rect x="9" y="11" width="14" height="10" fill="var(--white)"/><polyline points="9,11 16,17 23,11" fill="none" stroke="var(--black)" stroke-width="1.5"/></svg>
    <span>Email Id :<br>info@qBrightvoyage.com</span>
  </div>

  <h3 style="left:789px">Get In Touch</h3>
  <div class="field" style="top:125px">First Name</div>
  <div class="field" style="top:170px">Email Address</div>
  <div class="field" style="top:215px">Phone Number</div>
  <div class="field" style="top:258px;height:63px">Message :</div>
  <div class="submit">Submit</div>

  <p class="copyright">Copyright 2019 | All Rights Reserved | Privacy Policy | Term &amp; Conditions</p>
</footer>

</body>
</html>
```